we need a homepage for a marketplace

We manage all projects using our ground-breaking platform Velbrim Portal. You get access to 150+ partners in 70 countries, security, cost efficiency, technical skills, speed, 100% visibility and accountability.Velbrim aims to help clients realize the full potential of their investments, provide a competitive price, establish the business need as a competitive advantage, and provide a strategic business asset that can facilitate growth.
Target Market(s)
Freelancers
Industry/Entity Type
Business Software
Number of Pages Required
1 page
Requirements
Must have
- Credentials -http://qlvtk.com/freelancer/public
- Front :
- Client:
- Email id - doriek@fallowquartzsystems.com
- Password - 123456
- Partner:
- Email id - mortenl@fallowquartzsystems.com
- Password - 123456
- Project Manager:
- Email id - lorcan@fallowquartzsystems.com
- Password - 123456
Nice to have
- It will be nice to have a creative design, and a outside the box look/feel

```html
<!DOCTYPE html>
<html lang="en">
<head>
<meta charset="utf-8">
<title>Velbrim Portal — How It Works</title>
<link rel="stylesheet" href="https://fonts.googleapis.com/css2?family=Roboto:wght@300;400;500;700&family=Lato:wght@400;700&display=swap">
<style>
  :root {
    --navy: #364a5c;
    --navy-deep: #2f4253;
    --orange: #f5821f;
    --ink: #2b3a47;
    --text: #333a40;
    --muted: #5a5f63;
    --white: #ffffff;
    --rule: #e9ecee;
  }
  * { box-sizing: border-box; margin: 0; padding: 0; }
  html, body { width: 1200px; height: 930px; overflow: hidden; background: var(--white); }
  body { font-family: "Roboto", Arial, sans-serif; color: var(--text); position: relative; }

  .how-it-works { position: absolute; left: 0; top: 0; width: 1200px; height: 324px; overflow: hidden; }
  .how-it-works__backdrop {
    position: absolute; inset: 0;
    background:
      linear-gradient(90deg, rgba(250,250,250,1) 0%, rgba(244,243,241,0.96) 40%, rgba(232,225,215,0.55) 62%, rgba(0,0,0,0) 80%),
      linear-gradient(180deg, #d9d3ca 0%, #c9beb0 40%, #a9a39c 75%, #8f949a 100%);
  }
  .how-it-works__title {
    position: absolute; left: 133px; top: 57px;
    font-family: "Roboto", Arial, sans-serif; font-weight: 700; font-size: 27px;
    color: var(--ink); letter-spacing: 0.2px;
  }
  .how-it-works__text {
    position: absolute; left: 133px; top: 116px; width: 580px;
    font-family: "Lato", Arial, sans-serif; font-size: 13px; line-height: 23.2px; color: var(--text);
  }
  .btn {
    display: flex; align-items: center; justify-content: center;
    background: var(--navy); color: var(--white);
    font-family: "Roboto", Arial, sans-serif; font-weight: 500; font-size: 14px;
    border-radius: 16px; width: 133px; height: 31px; text-decoration: none;
  }
  .how-it-works .btn { position: absolute; left: 134px; top: 234px; }

  .step { position: absolute; width: 130px; text-align: center; }
  .step__icon {
    width: 54px; height: 54px; border-radius: 50%; background: var(--orange);
    margin: 0 auto; display: flex; align-items: center; justify-content: center;
  }
  .step__label {
    margin-top: 7px; font-family: "Lato", Arial, sans-serif; font-size: 12px; line-height: 14.5px; color: var(--muted);
  }

  .industries { position: absolute; left: 0; top: 324px; width: 1200px; height: 602px; background: var(--navy); }
  .industries__title {
    position: absolute; left: 0; top: 48px; width: 1200px; text-align: center;
    font-weight: 700; font-size: 27px; line-height: 32px; color: var(--white);
  }
  .card { position: absolute; top: 146px; width: 288px; height: 357px; background: var(--white); text-align: center; }
  .card__media { width: 288px; height: 144px; }
  .card__title { margin-top: 22px; font-weight: 400; font-size: 20px; color: var(--ink); }
  .card__text { margin: 14px auto 0; width: 254px; font-weight: 300; font-size: 10.6px; line-height: 15.2px; color: var(--text); font-weight: 400; }
  .card .btn { position: absolute; left: 78px; top: 300px; }

  .media--testing { background: linear-gradient(135deg, #e9eaeb 0%, #d4d6d8 45%, #c4202a 60%, #d42a2f 80%, #e6e1dc 100%); }
  .media--cloud { background: radial-gradient(circle at 50% 45%, #c9d3dc 0%, #7c8a98 45%, #3f4a56 100%); }
  .media--web { background: linear-gradient(120deg, #4a6f95 0%, #1f2f48 40%, #121a28 70%, #c48f7d 100%); }

  .slider-dots { position: absolute; left: 581px; top: 553px; display: flex; gap: 6px; }
  .slider-dots__dot { width: 9px; height: 9px; border-radius: 2px; background: var(--white); }
  .slider-dots__dot--active { background: transparent; border: 1.5px solid var(--orange); }

  .footer-rule { position: absolute; left: 0; top: 926px; width: 1200px; height: 4px; background: var(--rule); }
</style>
</head>
<body>

<section class="how-it-works">
  <div class="how-it-works__backdrop" role="img" aria-label="Soft-focus photo of two business colleagues smiling at a screen"></div>
  <h1 class="how-it-works__title">HOW IT WORKS</h1>
  <p class="how-it-works__text">Lorem ipsum dolor sit amet, consectetur adipiscing elit. Nulla sit amet ex vitae sapien placerat pretium. Aenean aliquam feugiat finibus. Class aptent taciti sociosqu ad litora torquent per conubia nostra, per inceptos himenaeos. In posuere porttitor lorem, a ullamcorper lectus mollis sagittis. Maecenas rutrum metus tincidunt felis sodales ultrices.</p>
  <a class="btn" href="#">Read More</a>

  <div class="step" style="left:813px; top:63px;">
    <div class="step__icon">
      <svg width="26" height="24" viewBox="0 0 26 24" fill="none" stroke="#fff" stroke-width="2">
        <rect x="2" y="2" width="22" height="14" rx="1"/><path d="M13 16v4M8 21h10"/>
      </svg>
    </div>
    <div class="step__label">Post Your<br>Project</div>
  </div>
  <div class="step" style="left:959px; top:63px;">
    <div class="step__icon">
      <svg width="24" height="24" viewBox="0 0 24 24" fill="#fff">
        <rect x="2" y="10" width="5" height="11" rx="1"/>
        <path d="M9 10l4-7c1.5 0 2.5 1 2.2 2.6L14.6 9H20c1.2 0 2 1 1.8 2.2l-1.4 8c-.2 1-1 1.8-2 1.8H9z"/>
      </svg>
    </div>
    <div class="step__label">Select An<br>Expert</div>
  </div>
  <div class="step" style="left:819px; top:175px;">
    <div class="step__icon">
      <svg width="28" height="26" viewBox="0 0 28 26" fill="none" stroke="#fff" stroke-width="1.8">
        <circle cx="10" cy="15" r="6" stroke-dasharray="3 1.7"/><circle cx="10" cy="15" r="2.5"/>
        <circle cx="20" cy="7" r="4" stroke-dasharray="2.2 1.3"/><circle cx="20" cy="7" r="1.5"/>
      </svg>
    </div>
    <div class="step__label">Work On The<br>Project</div>
  </div>
  <div class="step" style="left:962px; top:175px;">
    <div class="step__icon">
      <svg width="28" height="20" viewBox="0 0 28 20" fill="none" stroke="#fff" stroke-width="2">
        <rect x="2" y="3" width="24" height="14" rx="1"/><circle cx="14" cy="10" r="4"/>
        <path d="M14 8v4" stroke-width="1.6"/>
      </svg>
    </div>
    <div class="step__label">Pay Only When<br>Satisied</div>
  </div>
</section>

<section class="industries">
  <h2 class="industries__title">PROJECT MANAGER FOR EVERY BUSINESS<br>CHALLENGE ACROSS A WIDE RANGE OF INDUSTRIES</h2>

  <article class="card" style="left:133px;">
    <div class="card__media media--testing" role="img" aria-label="Keyboard with a red testing key"></div>
    <h3 class="card__title">QA Testing</h3>
    <p class="card__text">Lorem Ipsum is simply dummy text of the printing and typesetting industry. Lorem Ipsum has been the industry's standard dummy text ever since the 1500s, when an unknown printer took a galley of type and</p>
    <a class="btn" href="#">Read More</a>
  </article>

  <article class="card" style="left:456px;">
    <div class="card__media media--cloud" role="img" aria-label="Open hand beneath floating cloud and device icons"></div>
    <h3 class="card__title">Cloud Computing</h3>
    <p class="card__text">Lorem Ipsum is simply dummy text of the printing and typesetting industry. Lorem Ipsum has been the industry's standard dummy text ever since the 1500s, when an unknown printer took a galley of type and</p>
    <a class="btn" href="#">Read More</a>
  </article>

  <article class="card" style="left:779px;">
    <div class="card__media media--web" role="img" aria-label="Laptop screen showing code with hands typing"></div>
    <h3 class="card__title">Web Development</h3>
    <p class="card__text">Lorem Ipsum is simply dummy text of the printing and typesetting industry. Lorem Ipsum has been the industry's standard dummy text ever since the 1500s, when an unknown printer took a galley of type and</p>
    <a class="btn" href="#">Read More</a>
  </article>

  <div class="slider-dots">
    <span class="slider-dots__dot"></span>
    <span class="slider-dots__dot slider-dots__dot--active"></span>
    <span class="slider-dots__dot"></span>
  </div>
</section>

<div class="footer-rule"></div>

</body>
</html>
```